Marrowgate Auctions Business Cards Design Needed

I need a business card design that is modern looking - double sided (maybe just my logo on the back, but open to suggestions) - the overall design is up to you. I want it to be easy to read - not over the top flashy. I already have a company logo which I uploaded so that needs to be used. The colors of my logo are the colors I want on the card... so blue and gray (do need to match the logo colors).

Requirements
Must have
• Would like the card to be sleek, modern and easy to ready

```html
<!DOCTYPE html>
<html lang="en">
<head>
<meta charset="utf-8">
<title>Marrowgate Auctions Business Cards</title>
<link href="https://fonts.googleapis.com/css2?family=Montserrat:wght@400;600;700&display=swap" rel="stylesheet">
<style>
  :root {
    --brand-blue: #1e77c0;
    --brand-gray: #4a4c50;
    --text-gray: #5a5c60;
    --rule-gray: #6b6d70;
    --card-white: #ffffff;
    --backdrop: #2a2d31;
  }
  * { box-sizing: border-box; margin: 0; padding: 0; }
  html, body { width: 1200px; height: 960px; overflow: hidden; }
  body {
    background: var(--backdrop);
    font-family: "Montserrat", Arial, sans-serif;
    display: flex;
    align-items: center;
    justify-content: center;
    gap: 40px;
  }
  .card {
    position: relative;
    width: 540px;
    height: 310px;
    background: var(--card-white);
    border-radius: 22px;
    overflow: hidden;
  }
  .brand {
    display: flex;
    align-items: center;
    gap: 10px;
  }
  .brand-mark {
    width: 16px;
    height: 16px;
    border-radius: 50%;
    background: var(--brand-blue);
    flex: none;
  }
  .brand-name {
    font-weight: 700;
    color: var(--brand-gray);
    text-transform: uppercase;
    letter-spacing: 0.5px;
    line-height: 1.15;
  }
  /* Front */
  .card-front .brand {
    position: absolute;
    left: 34px;
    top: 70px;
    width: 200px;
  }
  .card-front .brand-name { font-size: 22px; }
  .divider {
    position: absolute;
    left: 262px;
    top: 36px;
    width: 2px;
    height: 190px;
    background: var(--rule-gray);
  }
  .contact {
    position: absolute;
    left: 286px;
    top: 58px;
    right: 16px;
  }
  .contact-name {
    font-size: 26px;
    font-weight: 700;
    color: var(--brand-blue);
    line-height: 1.1;
  }
  .contact-role {
    font-size: 12px;
    color: var(--text-gray);
    margin: 4px 0 14px;
  }
  .contact-list { list-style: none; }
  .contact-list li {
    display: flex;
    align-items: center;
    gap: 8px;
    font-size: 13.5px;
    color: var(--text-gray);
    line-height: 1.7;
  }
  .contact-list svg { width: 13px; height: 13px; flex: none; fill: var(--brand-blue); }
  .tagline-band {
    position: absolute;
    left: 0; right: 0; bottom: 0;
    height: 50px;
    background: var(--brand-blue);
    display: flex;
    align-items: center;
    padding-left: 36px;
  }
  .tagline {
    color: var(--card-white);
    font-size: 15px;
    letter-spacing: 0.3px;
  }
  /* Back */
  .card-back {
    display: flex;
    align-items: center;
    justify-content: center;
  }
  .card-back .brand-mark { width: 22px; height: 22px; }
  .card-back .brand-name { font-size: 30px; }
</style>
</head>
<body>
  <section class="card card-front" aria-label="Business card front">
    <div class="brand">
      <span class="brand-mark"></span>
      <span class="brand-name">Marrowgate Auctions</span>
    </div>
    <div class="divider"></div>
    <div class="contact">
      <p class="contact-name">Glen Harrow</p>
      <p class="contact-role">Owner / President - Auctioneer</p>
      <ul class="contact-list">
        <li>
          <svg viewBox="0 0 24 24" aria-hidden="true"><path d="M6.6 10.8a15 15 0 0 0 6.6 6.6l2.2-2.2c.3-.3.7-.4 1-.2 1.1.4 2.3.6 3.6.6.6 0 1 .4 1 1V20c0 .6-.4 1-1 1A17 17 0 0 1 3 4c0-.6.4-1 1-1h3.5c.6 0 1 .4 1 1 0 1.3.2 2.5.6 3.6.1.3 0 .7-.2 1z"/></svg>
          702-555-0148
        </li>
        <li>
          <svg viewBox="0 0 24 24" aria-hidden="true"><path d="M2 5h20v14H2zm2 2v.4l8 5 8-5V7zm0 2.8V17h16V9.8l-8 5z"/></svg>
          marrowgateauctions@mail.com
        </li>
        <li>
          <svg viewBox="0 0 24 24" aria-hidden="true"><path d="M12 2a10 10 0 1 0 0 20 10 10 0 0 0 0-20zm6.9 9h-3a15 15 0 0 0-1.3-5.9A8 8 0 0 1 18.9 11zM12 4.1c.9 1.2 1.8 3.6 1.9 6.9h-3.8c.1-3.3 1-5.7 1.9-6.9zM9.4 5.1A15 15 0 0 0 8.1 11h-3a8 8 0 0 1 4.3-5.9zM5.1 13h3a15 15 0 0 0 1.3 5.9A8 8 0 0 1 5.1 13zm6.9 6.9c-.9-1.2-1.8-3.6-1.9-6.9h3.8c-.1 3.3-1 5.7-1.9 6.9zm2.6-1A15 15 0 0 0 15.9 13h3a8 8 0 0 1-4.3 5.9z"/></svg>
          charitygavel.com
        </li>
      </ul>
    </div>
    <div class="tagline-band">
      <p class="tagline">Improving Charity Auctions Nationwide</p>
    </div>
  </section>

  <section class="card card-back" aria-label="Business card back">
    <div class="brand">
      <span class="brand-mark"></span>
      <span class="brand-name">Marrowgate Auctions</span>
    </div>
  </section>
</body>
</html>
```